Maple Junction: PowerPoint Design Project

I'm looking for a PowerPoint design that my real estate ompany will use for business proposals and presentations.
Updates

Project Deadline Extended
Reason: I'm making the contest "guaranteed payment" as requested by some designers. I'll be using the PowerPoint slides for client presentations. The tag lines given can be a footer or watermark because it just give an idea of what we do and what our company values are.

Target Market(s)

Landlords and corporate companies

Industry/Entity Type

Real Estate

Requirements
Must have
• Company logo
Various Tag lines as a part of the design of the PowerPoint:
1st tagline: we don't just build your business, we build your community
2nd tag line: we excel in generating revenue, enhancing the guest experience and protecting the brand.
3rd tag line: we are all about people, projects and profits

```html
<!DOCTYPE html>
<html lang="en">
<head>
<meta charset="utf-8">
<title>Maple Junction Property Consultants – Title Slide</title>
<link href="https://fonts.googleapis.com/css2?family=Open+Sans:wght@400;600;700&display=swap" rel="stylesheet">
<style>
  :root {
    --bg-top: #d6d6d6;
    --bg-mid: #e8e8e8;
    --bg-bottom: #fefefe;
    --brand-purple: #5a1199;
    --brand-green: #4a9a3a;
    --ribbon-green: rgba(150, 205, 150, 0.35);
    --ink-dark: #333333;
    --ink-soft: #666666;
    --ink-black: #1a1a1a;
    --rule: #ffffff;
    --button-grey: #b0b0b0;
    --button-text: #ffffff;
  }
  html, body {
    margin: 0;
    padding: 0;
    width: 1200px;
    height: 900px;
    overflow: hidden;
  }
  .slide {
    position: relative;
    width: 1200px;
    height: 900px;
    overflow: hidden;
    background: linear-gradient(to bottom, var(--bg-top) 0%, var(--bg-mid) 45%, var(--bg-bottom) 100%);
    font-family: "Open Sans", Arial, sans-serif;
  }
  .ribbon-decoration {
    position: absolute;
    top: -120px;
    right: -160px;
    width: 900px;
    height: 700px;
    background: radial-gradient(ellipse 60% 35% at 55% 30%, var(--ribbon-green) 0%, rgba(150,205,150,0.12) 55%, rgba(150,205,150,0) 100%);
    transform: rotate(18deg);
  }
  .brand {
    position: absolute;
    top: 40px;
    left: 0;
    width: 1200px;
    text-align: center;
  }
  .brand-mark {
    display: block;
    margin: 0 auto 16px;
  }
  .brand-name {
    margin: 0;
    font-size: 23px;
    font-weight: 700;
    color: var(--brand-purple);
    line-height: 1.1;
  }
  .brand-tagline {
    margin: 6px 0 0;
    font-size: 12.5px;
    font-weight: 600;
    color: var(--ink-black);
    letter-spacing: 0.3px;
  }
  .header-rule {
    position: absolute;
    top: 203px;
    left: 102px;
    width: 996px;
    height: 1px;
    background: var(--rule);
    border-top: 1px solid #c8c8c8;
  }
  .header-shadow {
    position: absolute;
    top: 205px;
    left: 102px;
    width: 996px;
    height: 80px;
    background: radial-gradient(ellipse 50% 100% at 50% 0%, rgba(0,0,0,0.09) 0%, rgba(0,0,0,0) 100%);
  }
  .title-block {
    position: absolute;
    top: 405px;
    left: 0;
    width: 1200px;
    text-align: center;
  }
  .headline {
    margin: 0;
    font-size: 24.5px;
    font-weight: 700;
    color: var(--ink-dark);
  }
  .subtitle {
    margin: 10px 0 0;
    font-size: 19.5px;
    font-weight: 400;
    color: var(--ink-soft);
  }
  .go-button {
    position: absolute;
    top: 734px;
    left: 564px;
    width: 74px;
    height: 74px;
    border-radius: 50%;
    background: var(--button-grey);
    color: var(--button-text);
    font-size: 38px;
    font-weight: 700;
    line-height: 74px;
    text-align: center;
    letter-spacing: -1px;
  }
</style>
</head>
<body>
  <main class="slide">
    <div class="ribbon-decoration" role="img" aria-label="Soft flowing green ribbon decoration"></div>

    <header class="brand">
      <svg class="brand-mark" width="60" height="60" viewBox="0 0 60 60" aria-hidden="true">
        <circle cx="30" cy="30" r="28" fill="var(--brand-green)"/>
      </svg>
      <p class="brand-name">Maple Junction Property Consultants</p>
      <p class="brand-tagline">Experiential Retail And Turn Around Professionals</p>
    </header>

    <div class="header-rule"></div>
    <div class="header-shadow"></div>

    <section class="title-block">
      <h1 class="headline">INSERT YOUR HEADLINE HERE, WITH CAPITAL FONT</h1>
      <p class="subtitle">This is Sample Text And Insert Your Subtitle Here for Your Bussiness</p>
    </section>

    <div class="go-button">GO</div>
  </main>
</body>
</html>
```